Smart, Classy, Conservative looking Legal Letterhead

I need a letterhead that when you look at it it "says to you " this is a well established law firm with very smart lawyers, which will one day be appearing before the Grand Bench of the USA. All information about the Law firm should appear at the top of the page. please no information in the footer.

Legal

• The name of the law firm, both addresses, phone number and fax,, The names of the attorneys, the website.
• Fields that get changed such as the date, VIA, Address of who the letter is going to,
• Re, Index,
• should have a clean neat look, sleek
• some color would be nice. A logo of some sort could be nice as well. Maybe a single S or interlocking D's For Dorvik and Dorvik.
• not too modern looking.

```html
<!DOCTYPE html>
<html lang="en">
<head>
<meta charset="utf-8">
<title>Dorvik &amp; Dorvik, LLC — Stationery</title>
<link href="https://fonts.googleapis.com/css2?family=Cinzel:wght@400;500&family=Didact+Gothic&display=swap" rel="stylesheet">
<style>
  :root {
    --brand-blue: #0a5b7e;
    --brand-blue-light: #136a8f;
    --rule-grey: #a3a3a3;
    --paper: #ffffff;
    --backdrop: #cbcbcb;
    --ink: #3b3b3b;
    --ink-soft: #6a6a6a;
    --serif: "Cinzel", "Times New Roman", serif;
    --sans: "Didact Gothic", "Century Gothic", sans-serif;
  }
  * { box-sizing: border-box; margin: 0; padding: 0; }
  html, body { width: 1200px; height: 1000px; overflow: hidden; }
  body { background: var(--backdrop); position: relative; font-family: var(--sans); color: var(--ink); }

  .piece { position: absolute; background: var(--paper); box-shadow: 0 2px 4px rgba(0,0,0,.25); }

  /* brand lockup */
  .lockup { position: absolute; display: flex; align-items: flex-start; gap: 7px; }
  .lockup__mark { background: var(--brand-blue); flex: none; }
  .lockup__text { display: flex; flex-direction: column; }
  .lockup__name { font-family: var(--serif); color: var(--brand-blue); white-space: nowrap; border-bottom: 1px solid var(--ink-soft); line-height: 1.15; }
  .lockup__tag { font-family: var(--serif); color: var(--ink); white-space: nowrap; line-height: 1.3; }
  .lockup--reverse .lockup__name, .lockup--reverse .lockup__tag { color: #fff; border-color: rgba(255,255,255,.8); }
  .lockup--reverse .lockup__mark { background: #fff; }

  /* top bands */
  .band { position: absolute; top: 0; height: 6px; }
  .band--blue { background: var(--brand-blue); }
  .band--grey { background: var(--rule-grey); }

  /* folder */
  .folder { left: 152px; top: 40px; width: 431px; height: 560px; border-radius: 4px;
    background: linear-gradient(160deg, var(--brand-blue-light), var(--brand-blue) 60%); }
  .folder__spine { position: absolute; top: 0; bottom: 0; width: 1px; background: rgba(0,0,0,.25); }

  /* letterhead */
  .letterhead { left: 616px; top: 60px; width: 417px; height: 540px; }
  .letterhead__attorneys { position: absolute; left: 25px; top: 67px; font-size: 5.2px; line-height: 7px; letter-spacing: .2px; color: var(--ink-soft); text-transform: uppercase; }
  .letterhead__contact { position: absolute; right: 24px; top: 28px; font-size: 5.2px; line-height: 6.4px; text-align: right; color: var(--ink-soft); }
  .letterhead__contact b { color: var(--brand-blue); font-weight: normal; }
  .letterhead__office { margin-top: 6px; }
  .letterhead__office-title { color: var(--brand-blue); text-transform: uppercase; }

  /* envelopes */
  .envelope { left: 116px; top: 629px; width: 439px; height: 202px; }
  .envelope__return { position: absolute; left: 24px; bottom: 9px; font-size: 5.2px; line-height: 6.4px; color: var(--ink-soft); }
  .envelope-back { left: 616px; top: 629px; width: 438px; height: 202px; overflow: hidden; }
  .envelope-back svg { position: absolute; left: 0; top: 0; }
  .envelope-back__mark { position: absolute; left: 213px; top: 26px; width: 12px; height: 12px; background: #fff; }

  /* business cards */
  .card { top: 861px; width: 172px; height: 98px; }
  .card--front { left: 410px; }
  .card--back { left: 616px; background: var(--brand-blue); }
  .card__person { position: absolute; left: 9px; top: 54px; font-size: 5.4px; color: var(--brand-blue); text-transform: uppercase; }
  .card__details { position: absolute; left: 9px; top: 69px; font-size: 4.4px; line-height: 5.6px; color: var(--ink-soft); }
  .card__details b { color: var(--brand-blue); font-weight: normal; }
  .card__address { position: absolute; right: 9px; top: 74px; font-size: 4.4px; line-height: 5.4px; text-align: right; color: var(--ink-soft); }
</style>
</head>
<body>

  <!-- Presentation folder -->
  <section class="piece folder" aria-label="Presentation folder">
    <span class="folder__spine" style="left:18px"></span>
    <span class="folder__spine" style="left:26px"></span>
    <div class="lockup lockup--reverse" style="left:96px; top:89px;">
      <span class="lockup__mark" style="width:12px;height:12px;margin-top:3px;"></span>
      <div class="lockup__text">
        <span class="lockup__name" style="font-size:13.5px;">Dorvik &amp; Dorvik, LLC</span>
        <span class="lockup__tag" style="font-size:9px;">Attorneys at Law</span>
      </div>
    </div>
  </section>

  <!-- Letterhead -->
  <section class="piece letterhead" aria-label="Letterhead">
    <span class="band band--blue" style="left:0;width:256px;"></span>
    <span class="band band--grey" style="left:260px;right:0;"></span>
    <div class="lockup" style="left:25px; top:28px;">
      <span class="lockup__mark" style="width:9px;height:9px;margin-top:2px;"></span>
      <div class="lockup__text">
        <span class="lockup__name" style="font-size:10.5px;">Dorvik &amp; Dorvik, LLC</span>
        <span class="lockup__tag" style="font-size:7px;">Attorneys at Law</span>
      </div>
    </div>
    <div class="letterhead__attorneys">
      Martin Dorvik, Esq.<br>
      Dennis A. Dorvik, Esq.<br>
      Eleanor Whitcombe, Esq.<br>
      Paul T. Marsh, Esq.*<br>
      *Admitted in NY &amp; MA
    </div>
    <address class="letterhead__contact" style="font-style:normal;">
      48 Hollis Street<br>
      New York, New York 10007<br>
      <b>Tel:</b> 555-201-4830 · <b>Fax:</b> 555-201-4831<br>
      <b>Email:</b> Dennis.Dorvik@dorviklegal.com<br>
      www.dorvikconsumerlaw.com
      <div class="letterhead__office">
        <span class="letterhead__office-title">Northfield Office</span><br>
        215 Alder Road<br>
        Millbrook<br>
        New York 10580
      </div>
    </address>
  </section>

  <!-- Envelope front -->
  <section class="piece envelope" aria-label="Envelope front">
    <span class="band band--blue" style="left:0;width:257px;"></span>
    <span class="band band--grey" style="left:261px;right:0;"></span>
    <div class="lockup" style="left:24px; top:28px;">
      <span class="lockup__mark" style="width:9px;height:9px;margin-top:2px;"></span>
      <div class="lockup__text">
        <span class="lockup__name" style="font-size:10.5px;">Dorvik &amp; Dorvik, LLC</span>
        <span class="lockup__tag" style="font-size:7px;">Attorneys at Law</span>
      </div>
    </div>
    <address class="envelope__return" style="font-style:normal;">
      48 Hollis Street<br>New York, New York 10007
    </address>
  </section>

  <!-- Envelope back -->
  <section class="piece envelope-back" aria-label="Envelope back">
    <svg width="438" height="202" viewBox="0 0 438 202" aria-hidden="true">
      <polygon points="0,0 438,0 438,6 425,92 13,92 0,6" fill="var(--brand-blue)"/>
    </svg>
    <span class="envelope-back__mark"></span>
  </section>

  <!-- Business card front -->
  <section class="piece card card--front" aria-label="Business card front">
    <span class="band band--blue" style="left:0;width:90px;height:3px;"></span>
    <span class="band band--grey" style="left:93px;right:0;height:3px;"></span>
    <div class="lockup" style="left:9px; top:17px; gap:4px;">
      <span class="lockup__mark" style="width:6px;height:6px;margin-top:2px;"></span>
      <div class="lockup__text">
        <span class="lockup__name" style="font-size:7.4px;">Dorvik &amp; Dorvik, LLC</span>
        <span class="lockup__tag" style="font-size:4.8px;">Attorneys at Law</span>
      </div>
    </div>
    <div class="card__person">Martin Dorvik, Esq.</div>
    <div class="card__details">
      <b>T</b> 555-201-4830<br>
      <b>F</b> 555-201-4831<br>
      <b>E</b> Martin.Dorvik@dorviklegal.com<br>
      <b>W</b> www.dorvikconsumerlaw.com
    </div>
    <address class="card__address" style="font-style:normal;">
      48 Hollis Street<br>New York<br>New York 10007
    </address>
  </section>

  <!-- Business card back -->
  <section class="piece card card--back" aria-label="Business card back">
    <div class="lockup lockup--reverse" style="left:20px; top:40px; gap:4px;">
      <span class="lockup__mark" style="width:7px;height:7px;margin-top:2px;"></span>
      <div class="lockup__text">
        <span class="lockup__name" style="font-size:7.6px;">Dorvik &amp; Dorvik, LLC</span>
        <span class="lockup__tag" style="font-size:4.8px;">Attorneys at Law</span>
      </div>
    </div>
  </section>

</body>
</html>
```